Business Card for Start-Up Consulting Business
TK Advisory Partners, LLC
Business Card for Start-Up Consulting Business - Consulting
Creative Brief
Professional
Roderick Lyle Pemberton
President/CEO
82 Fenwhistle Court #2410 Dover, DE 19906
info@tkapllc.example
www.tkapllc.example
On the back of the card, I would like something like: Text TKTEAM to 38217 for updates and promotions or For updates and promotions, text TKTEAM to 38217. I would also like to have our services listed on the back of the card like: We Specialize In: or Our Services Includes: *Negative Equity Financing *Tax Mitigation *Life & Health Insurance *Merchant Processing *Telecommunications *Energy Saving Programs *Marketing & Advertising and *More. And if the back is not crowded, maybe we can added the phone, fax, email and/or web address. Thanks

```html
<!DOCTYPE html>
<html lang="en">
<head>
<meta charset="utf-8">
<title>TK Advisory Partners, LLC — Business Card</title>
<link href="https://fonts.googleapis.com/css2?family=Cinzel:wght@400;600;700&family=Amiri:wght@400&display=swap" rel="stylesheet">
<style>
  :root{
    --page:#e9e9e9;
    --card-white:#ffffff;
    --card-mist:#eef0f3;
    --navy:#1f3f7c;
    --navy-deep:#15295a;
    --navy-light:#3b66ad;
    --green:#5aa631;
    --green-light:#8cc63f;
    --ink:#2b3f73;
    --text-light:#f3f5fa;
  }
  *{margin:0;padding:0;box-sizing:border-box}
  html,body{width:1200px;height:770px;overflow:hidden;background:var(--page)}
  .card{
    position:relative;width:1200px;height:770px;border-radius:44px;overflow:hidden;
    background:radial-gradient(ellipse at 50% 20%,var(--card-white) 40%,var(--card-mist) 100%);
    font-family:"Cinzel",serif;
  }
  .waves{position:absolute;inset:0;width:100%;height:100%}
  .brand{position:absolute;left:290px;top:92px;display:flex;align-items:flex-start;gap:24px}
  .brand-square{width:72px;height:72px;background:var(--green);margin-top:22px}
  .brand-text{display:flex;flex-direction:column}
  .blessing{
    display:flex;align-items:center;gap:10px;font-family:"Amiri",serif;font-size:30px;
    color:var(--ink);line-height:1;direction:rtl;
  }
  .blessing::before,.blessing::after{content:"";display:block;width:60px;height:2px;background:var(--ink)}
  .company-name{font-size:46px;font-weight:600;color:var(--navy);letter-spacing:1px;line-height:1.15;margin-top:6px}
  .tagline{font-size:27px;font-weight:700;color:var(--green);letter-spacing:.5px;margin-top:2px}
  .contacts{position:absolute;left:40px;top:440px;list-style:none;color:var(--text-light);font-size:17px;line-height:26px;letter-spacing:.5px}
  .contacts li{display:flex;align-items:flex-start;gap:10px}
  .contacts .indent{padding-left:28px;margin-top:-2px}
  .icon{flex:none;width:18px;height:18px;margin-top:4px}
  .person{position:absolute;right:64px;top:632px;text-align:right;color:var(--text-light)}
  .person-name{font-size:30px;font-weight:400;letter-spacing:1px}
  .person-title{font-size:24px;margin-top:8px;letter-spacing:.5px}
</style>
</head>
<body>
<div class="card">
  <svg class="waves" viewBox="0 0 1200 770" preserveAspectRatio="none" aria-hidden="true">
    <defs>
      <linearGradient id="navyFill" x1="0" y1="0" x2="0" y2="1">
        <stop offset="0" stop-color="var(--navy-light)"/>
        <stop offset=".45" stop-color="var(--navy)"/>
        <stop offset="1" stop-color="var(--navy-deep)"/>
      </linearGradient>
      <linearGradient id="greenFill" x1="0" y1="0" x2="1" y2="0">
        <stop offset="0" stop-color="var(--green-light)"/>
        <stop offset=".5" stop-color="var(--green)"/>
        <stop offset="1" stop-color="var(--green-light)"/>
      </linearGradient>
    </defs>
    <path d="M0 300 C 260 320, 600 470, 820 540 C 980 585, 1100 585, 1200 570 L1200 770 L0 770 Z" fill="url(#navyFill)"/>
    <path d="M0 282 C 300 290, 650 430, 900 455 C 1030 467, 1120 440, 1200 400 C 1120 470, 1010 500, 880 492 C 640 478, 320 330, 0 312 Z" fill="url(#greenFill)"/>
    <path d="M120 330 C 420 380, 720 520, 1000 540 C 1090 546, 1150 530, 1200 505" fill="none" stroke="var(--green)" stroke-width="6"/>
    <path d="M300 400 C 560 480, 800 560, 1010 565 C 1100 567, 1160 550, 1200 535" fill="none" stroke="var(--green-light)" stroke-width="3"/>
  </svg>

  <header class="brand">
    <div class="brand-square"></div>
    <div class="brand-text">
      <div class="blessing">بسم الله الرحمن الرحيم</div>
      <div class="company-name">TK Advisory Partners, LLC</div>
      <div class="tagline">Helping Businesses Save Money!</div>
    </div>
  </header>

  <ul class="contacts">
    <li><svg class="icon" viewBox="0 0 18 18"><circle cx="9" cy="9" r="9" fill="#fff"/><path d="M9 3.5a3.5 3.5 0 0 0-3.5 3.5c0 2.6 3.5 7 3.5 7s3.5-4.4 3.5-7A3.5 3.5 0 0 0 9 3.5zm0 4.8a1.3 1.3 0 1 1 0-2.6 1.3 1.3 0 0 1 0 2.6z" fill="var(--navy)"/></svg>82 Fenwhistle Court #2410</li>
    <li class="indent">Dover, DE 19906</li>
    <li><svg class="icon" viewBox="0 0 18 18"><circle cx="9" cy="9" r="9" fill="#fff"/><path d="M6 4.5l1.6 2.4-1 1.2a7 7 0 0 0 3.3 3.3l1.2-1 2.4 1.6-.9 1.7C8.8 13.5 4.5 9.2 4.3 5.4z" fill="var(--navy)"/></svg>(302) 555-0148</li>
    <li><svg class="icon" viewBox="0 0 18 18"><circle cx="9" cy="9" r="9" fill="#fff"/><rect x="6" y="3.5" width="6" height="11" rx="1" fill="var(--navy)"/></svg>(302) 555-0172</li>
    <li><svg class="icon" viewBox="0 0 18 18"><circle cx="9" cy="9" r="9" fill="#fff"/><path d="M6 4.5l1.6 2.4-1 1.2a7 7 0 0 0 3.3 3.3l1.2-1 2.4 1.6-.9 1.7C8.8 13.5 4.5 9.2 4.3 5.4z" fill="var(--navy)"/></svg>(888) 555-0193</li>
    <li><svg class="icon" viewBox="0 0 18 18"><circle cx="9" cy="9" r="9" fill="#fff"/><rect x="4" y="5.5" width="10" height="7" fill="var(--navy)"/><path d="M4 5.5l5 4 5-4" fill="none" stroke="#fff" stroke-width="1"/></svg>info@tkapllc.example</li>
    <li><svg class="icon" viewBox="0 0 18 18"><circle cx="9" cy="9" r="9" fill="#fff"/><circle cx="9" cy="9" r="5" fill="none" stroke="var(--navy)" stroke-width="1.4"/><path d="M4 9h10M9 4c-2.5 3-2.5 7 0 10M9 4c2.5 3 2.5 7 0 10" fill="none" stroke="var(--navy)" stroke-width="1"/></svg>www.tkapllc.example</li>
  </ul>

  <div class="person">
    <div class="person-name">Roderick Lyle Pemberton</div>
    <div class="person-title">President/CEO</div>
  </div>
</div>
</body>
</html>
```